Research project presentation flyer

Pending approval of a cooperative research project we need a flyer to present and "market" the academic project to the businesses we want to invite to participate.

The project is a cooperation between three different universities and businesses in the Nordic/Baltic countries and the subject is innovation and entrepreneurship (see the attached "raw" edition).

The intended audience will be all those directly involved with the project, media, municipalities/government, businesses and also the public.

The flyer needs to be in multiple language-editions, but the design must of course be identical. For this designproject, we submit the English content (please correct the English in the attached proposal as necessary). Thus the project result must be in a format that allows us to replace the English text with other languages ourselves.

The proposal attached is just that: a laymans proposal (and the content). Please feel free to rearrange content (and redesign!)

The format of the flyer is a folded A4 (i.e. A5 portrait), with print on both sides.

The raw edition that is attached contains a map that is merely a suggestion (low quality). A better map - perhaps with less irrelevant detail - must be proposed. The important part of the map is to show the location of the universities and project office.

Also, the "logo" of the project is of low quality, and must be changed. A core concept of the project is "triple helix", so the "logo" of the project should be something to that effect (triple helix), as indicated. The "logo" is only an illustration to be used on the flyer. The aim is not to develop a logo for the project. We will do that at a later stage.

The flyer is supposed to be downloadable from a project web, both in hi-res for printing in a professional printshop, and for printing on an average office colour printer. Designs that bleeds off the paper-edge might therefore be a challenge, as office-printers don't print to the edge of the paper.

Reason: Due to Easter holiday and few submissons.

Printing

• Format: A4 folded once, i.e. A5 portrait
Must be able to alter text in design to produce flyers in other languages that English (i.e. pdf is good for the English version, but editable fileformat must also be submitted)
Map must be improved
Logo must be improved. Concept: triple helix
• Clean, professional design.
Flyer is "selling" an academic project that must appeal to businesses

```html
<!DOCTYPE html>
<html lang="en">
<head>
<meta charset="utf-8">
<title>Innovation and Entrepreneurship for Work Life – Flyer Cover</title>
<link rel="stylesheet" href="https://fonts.googleapis.com/css2?family=Cabin:wght@500;600;700&display=swap">
<style>
  :root {
    --stage: #dcdcdc;
    --paper: #ffffff;
    --ink-grey: #646464;
    --project-blue: #1aa3e0;
    --accent-gold: #e8d49a;
    --mark-tint: #f3e7c3;
  }
  * { box-sizing: border-box; margin: 0; padding: 0; }
  html, body {
    width: 1200px;
    height: 900px;
    overflow: hidden;
    background: var(--stage);
  }
  .canvas {
    position: relative;
    width: 1200px;
    height: 900px;
    display: flex;
    align-items: center;
    justify-content: center;
  }
  .flyer-cover {
    position: relative;
    width: 608px;
    height: 860px;
    background: var(--paper);
    font-family: "Cabin", "Candara", sans-serif;
    color: var(--ink-grey);
    text-align: center;
  }
  .project-mark {
    position: absolute;
    top: 125px;
    left: 50%;
    width: 150px;
    height: 150px;
    margin-left: -75px;
    border-radius: 50%;
    background: var(--mark-tint);
  }
  .project-name {
    position: absolute;
    top: 316px;
    left: 0;
    width: 100%;
    font-size: 34px;
    font-weight: 500;
    line-height: 1;
    letter-spacing: 0.03em;
    color: var(--project-blue);
  }
  .cover-title {
    position: absolute;
    top: 444px;
    left: 0;
    width: 100%;
    font-size: 41px;
    font-weight: 700;
    line-height: 39px;
  }
  .title-rule {
    position: absolute;
    top: 577px;
    left: 132px;
    width: 370px;
    height: 4px;
    background: var(--accent-gold);
  }
  .cover-summary {
    position: absolute;
    top: 603px;
    left: 0;
    width: 100%;
    font-size: 19.5px;
    font-weight: 600;
    line-height: 24.5px;
  }
</style>
</head>
<body>
  <main class="canvas">
    <article class="flyer-cover">
      <div class="project-mark"></div>
      <div class="project-name">Helixa</div>
      <h1 class="cover-title">Innovation and<br>Entrepreneurship<br>for Work Life</h1>
      <div class="title-rule"></div>
      <p class="cover-summary">A Nordic-Baltic cooperative project on the<br>development of innovation and<br>entrepreneurship in a symbiosis between<br>education, trade/industry and governmental<br>organisations.</p>
    </article>
  </main>
</body>
</html>
```